依頼詳細
社労士、行政書士としての一般的な業務のほか、農地転用や農業参入に力を入れたいとのことでウェブサイトを制作されることになりました。

掲載コンテンツが未定のため、グローバルメニューではいくつかのサブページを想定しておりますが、決定事項ではないため、トップ1ページ、サブ1ページの計2ページのデザイン制作です。
詳細は添付のワイヤーフレームをご覧ください。

▶︎デザインは各ページ、デスクトップ表示とモバイル表示の2つご用意ください。

▶︎モバイル表示時のメニューは、ハンバーガー推奨ですが、他でも可です。

▶︎デスクトップとモバイルの切り替えは、800pxを基準とします。

▶︎フォントはウェブで使用できるフォントに限ります。使用したフォントを明記してください。googleのウェブフォントは使用可。

▶︎テキストやキャッチコピーはアテの状態でかまいませんが、デザイン上必要であれば、仮に書いていただいても可、評価に加味いたします。

▶︎色合いは、緑〜青を基調を希望。 ただし逸脱しても可。

▶︎ご本人の姿は掲載不可のため、ご本人の写真を想定したデザインは避けてください。

▶︎イラスト調は可。

▶︎ロゴのようなものはありませんが、添付の画像を封筒や名刺に使われているので、参考にしてください。(そのまま使っても可。ただしベクターデータなし)

▶︎有料素材を使用する場合は、使用素材のリンクと総額を明記してください。

▶︎事務所内の写真など、現地での撮影を想定したものは、適当な素材を使用の上、素材上にその旨を明記してください。

▶︎納品は、aiデータ希望ですが、psdデータも可とします。

サイトURL
ページ数
2ページ
希望イメージ
シンプル 複雑
単色 カラフル
暗い 明るい
日常 高級
遊び心 厳粛
未来的 伝統的
女性的 男性的
希望する色
緑系、青系、水色系
納品ファイル
• イラストレーター形式 (.ai)
• フォトショップ形式 (.psd)
補足説明
ランサーの皆さま。
お世話になります。

納品は、モバイル表示のデザインもいただきたいですが、
コンペ参加はデスクトップ表示のみでもかまいません。
ぜひ、ふるってご参加のほど、よろしくお願いいたします。
ご提案いただきましたランサーの皆さま

このたびは、素敵なご提案をいただき、まことにありがとうございます。
弊社都合で申し訳ありませんが、選定会議の都合上、決定の選択は10月16日(金)以降にさせていただきます。
お時間いただきますが、よろしくお願いいたします。
■ 選んだ理由

写真の選択が素晴らしく、また機能としても整ってみえました。
弊社もお客様も満場一致でしたので、採択させていただきました。

■ 提案者全員のお礼・コメント

弊社の依頼にご提案いただきました皆さま、まことにありがとうございます。
また機会がございましたら、ご参加いただけますこと心よりお願い申し上げます。

```html
<!DOCTYPE html>
<html lang="ja">
<head>
<meta charset="utf-8">
<title>森川 社労士/行政書士 事務所</title>
<link rel="stylesheet" href="https://fonts.googleapis.com/css2?family=Noto+Sans+JP:wght@400;500;700&family=Noto+Serif+JP:wght@500;700&family=Cormorant+Garamond:ital,wght@1,500&display=swap">
<style>
:root{
  --ink:#2b2f33;
  --muted:#6b7278;
  --navy:#1c2433;
  --hero-sky:#c4e2f2;
  --hero-field:#a8cd7e;
  --tag:#cfe9f2;
  --tag-ink:#3a7d96;
  --line:#d8dde0;
  --band-a:#38b8d6;
  --band-b:#9be08a;
  --paper:#ffffff;
}
*{margin:0;padding:0;box-sizing:border-box}
html,body{width:859px;height:1200px;overflow:hidden}
body{position:relative;font-family:"Noto Sans JP",sans-serif;color:var(--ink);
  background:linear-gradient(180deg,#fff 0,#fff 600px,#f3f9f3 900px,#e8f3ec 1140px)}
.site-header{position:absolute;top:0;left:0;width:859px;height:44px;background:var(--paper);display:flex;align-items:center;z-index:3}
.brand{display:flex;align-items:center;gap:6px;padding-left:16px;font-family:"Noto Serif JP",serif;font-weight:700;font-size:13px;color:var(--navy)}
.brand small{font-size:8px;font-weight:700;line-height:1.1}
.global-nav{margin-left:auto;display:flex;gap:30px;font-size:9px;color:var(--ink);padding-right:30px}
.contact-btn{width:74px;height:44px;background:var(--navy);color:#fff;font-size:8px;display:flex;flex-direction:column;align-items:center;justify-content:center;gap:3px}
.hero{position:absolute;top:0;left:0;width:859px;height:550px;
  background:linear-gradient(180deg,var(--hero-sky) 0,#e3f1ee 55%,var(--hero-field) 85%,#fff 100%)}
.hero-copy{position:absolute;left:229px;top:157px;width:406px;height:116px;background:var(--paper);text-align:center;padding-top:22px}
.hero-copy h1{font-family:"Noto Serif JP",serif;font-weight:500;font-size:17px;letter-spacing:.18em;line-height:1.85}
.hero-copy p{font-family:"Cormorant Garamond",serif;font-style:italic;font-size:11px;color:var(--muted);margin-top:4px}
.intro{position:absolute;top:570px;left:218px;width:424px;font-size:8px;line-height:2.05;letter-spacing:.12em;color:var(--ink)}
.services{position:absolute;top:700px;left:223px;display:flex;gap:50px}
.service-card{width:177px;height:155px;position:relative}
.service-card .photo{width:100%;height:100%}
.service-card .label{position:absolute;left:38px;right:38px;bottom:16px;height:22px;background:var(--paper);font-size:8px;display:flex;align-items:center;justify-content:center;color:var(--ink)}
.news{position:absolute;top:912px;left:0;width:859px;text-align:center}
.news h2{font-family:"Noto Serif JP",serif;font-weight:500;font-size:15px;letter-spacing:.15em}
.news-list{list-style:none;margin:26px auto 0;width:300px;text-align:left}
.news-list li{display:flex;align-items:center;gap:8px;font-size:7.5px;height:19px}
.news-list time{color:var(--muted);width:44px}
.news-list .tag{background:var(--tag);color:var(--tag-ink);padding:1px 6px;font-size:7px}
.more-btn{position:absolute;top:1046px;left:340px;width:180px;height:30px;border:1px solid var(--line);background:var(--paper);font-size:8px;display:flex;align-items:center;justify-content:center;gap:50px}
.site-footer{position:absolute;bottom:0;left:0;width:859px;height:60px;background:var(--navy);color:#fff;display:flex;align-items:center}
.site-footer .brand{color:#fff;padding-left:16px}
.footer-address{font-size:6.5px;color:#c8ced6;margin-left:14px}
.footer-tel{position:absolute;right:0;top:0;width:360px;height:60px;background:linear-gradient(90deg,var(--band-a),var(--band-b));display:flex;align-items:center;justify-content:space-around;font-size:15px;font-weight:500;color:var(--navy)}
.footer-tel span small{font-size:7px;margin-right:4px}
</style>
</head>
<body>
<header class="site-header">
  <div class="brand"><span>森川</span><small>社労士/<br>行政書士</small><span>事務所</span></div>
  <nav class="global-nav"><span>事務所案内</span><span>農地転用・農業参入サービス</span><span>行政書士サービス</span><span>お知らせ</span></nav>
  <a class="contact-btn"><svg width="12" height="9" viewBox="0 0 12 9"><rect x=".5" y=".5" width="11" height="8" fill="none" stroke="#fff"/><path d="M.5 .5 6 5l5.5-4.5" fill="none" stroke="#fff"/></svg>お問い合わせ</a>
</header>

<section class="hero" role="img" aria-label="青空の下に広がる田園と遠くの山並みの写真">
  <div class="hero-copy">
    <h1>農地転用・農業参入は<br>おまかせください。</h1>
    <p>Morikawa Office</p>
  </div>
</section>

<p class="intro">地域の農地を守りながら、新しく農業を始めたい方や土地の活用を考える方を、書類作成から申請手続きまで丁寧にお手伝いいたします。農地の転用や売買、貸し借りに関する許可申請、農業法人の設立や新規参入の計画づくりなど、状況に合わせて最適な方法をご提案します。社会保険や労務のご相談、就業規則の作成、各種許認可の手続きもお気軽にどうぞ。初めての方にもわかりやすい説明を心がけ、ご相談から完了まで責任をもって対応いたします。地元に根ざした事務所として、皆さまの一歩を誠実に支えてまいります。</p>

<section class="services">
  <div class="service-card">
    <div class="photo" role="img" aria-label="実った稲穂の写真" style="background:linear-gradient(135deg,#c9b56a,#7f9f4a)"></div>
    <div class="label">農地転用</div>
  </div>
  <div class="service-card">
    <div class="photo" role="img" aria-label="収穫した色とりどりの野菜の写真" style="background:linear-gradient(135deg,#c9483a,#7aa84a 70%,#e3c15a)"></div>
    <div class="label">農業参入</div>
  </div>
</section>

<section class="news">
  <h2>お知らせ</h2>
  <ul class="news-list">
    <li><time>2020.00.00</time><span class="tag">お知らせ</span><span>年末年始の営業日についてのご案内です</span></li>
    <li><time>2020.00.00</time><span class="tag">お知らせ</span><span>無料相談会を開催いたします</span></li>
    <li><time>2020.00.00</time><span class="tag">お知らせ</span><span>ホームページを公開いたしました</span></li>
  </ul>
</section>
<a class="more-btn"><span>もっと見る</span><svg width="8" height="8" viewBox="0 0 8 8"><circle cx="4" cy="4" r="3.5" fill="none" stroke="#6b7278"/><path d="M3.3 2.5 4.8 4 3.3 5.5" fill="none" stroke="#6b7278"/></svg></a>

<footer class="site-footer">
  <div class="brand"><span>森川</span><small>社労士/<br>行政書士</small><span>事務所</span></div>
  <p class="footer-address">〒000-0000 長野県森川市緑町1-2-3 森川ビル2F</p>
  <div class="footer-tel"><span><small>TEL</small>0123-45-6789</span><span><small>FAX</small>0123-45-6780</span></div>
</footer>
</body>
</html>
```